Catering Company Website Design

We are working with a bbq catering company in California called Hickory Ember Catering.
Some sites to use for content/competitors and inspiration:
https://19turnips.example
https://brennafoxley.example
https://beyondfeasts.example
https://redbowlmarlow.example (client's favorite)
https://www.dorindasgrill.example (client's favorite)
https://www.thebrightsagekitchen.example
Thank you for taking the time to consider designing a website for us. We are web developers based in Stockton, CA, USA. Most of our projects go through the same process. Understanding this process may help you win a project with us. We custom-code all of our websites in-house. We don’t have any requirements as to what tools you use for your design, but we prefer Figma files. For any design that we label as four-stars, we send it to the client for review. The client picks the final design they want us to use. Once we complete this process, we will continue to show additional clients all the four-star sites and purchase them later. Your designs will have multiple chances to sell. For better chances of success, we ask that you follow these guidelines.
IMAGES:
If you use any images or icons in the design, we ask that you have a link to the asset so we can purchase the image/icon. Most of the designs we submit do not have the customer’s images on them unless they have some great images. Be creative; show us the feeling you are trying to portray with your image choices. Use any royalty-free site you choose. We subscribe to Adobe and mainly use their images, but we can purchase images outside of Adobe.
PLEASE NOTE: we will not submit designs to clients with watermarks on the images.
FONTS:
We ask that you identify the fonts used in the design. This can be done in a message if you want. We typically use Google Fonts and Adobe Fonts.
CONTENT:
We're always open to different content and ideas. We often submit designs with stock images so the client can see our vision. We typically take pictures after the website launch to use their images with our vision. Lorem Ipsum is fine for paragraphs, but we ask that you write the headers in correct English. We want to be able to show the vision and identify the sections of the website.
INSPIRATION:
We typically add a couple of links in the brief of websites we like to help you get started in your design.
REVISIONS:
We do not often ask for revisions of the designs unless we see something in the design that may not appeal to the client. If there are slight changes that we want to make, we do that in the development process.
FEEDBACK:
We rarely give feedback on designs during the design process. We are working on many website projects and do not have the time to provide feedback. We usually respond if your request is well thought out and asks specific questions, but a note asking “feedback, please” usually goes unanswered

```html
<!DOCTYPE html>
<html lang="en">
<head>
<meta charset="utf-8">
<title>Hickory Ember Catering</title>
<link rel="stylesheet" href="https://fonts.googleapis.com/css2?family=Poppins:wght@400;500;600&display=swap">
<style>
:root{
  --red:#e1261c;
  --brown:#3c2a1f;
  --black:#050505;
  --white:#ffffff;
  --ink:#222222;
}
*{box-sizing:border-box;margin:0;padding:0}
html,body{width:1200px;height:4027px;overflow:hidden}
body{position:relative;font-family:"Poppins",sans-serif;color:var(--ink);background:var(--white)}
h1,h2,h3{font-weight:400}
.abs{position:absolute}
.photo{position:absolute}
.btn{position:absolute;display:flex;align-items:center;justify-content:center;font-size:16px;font-weight:500}
.btn-red{background:var(--red);color:var(--white)}
.btn-white{background:var(--white);color:var(--red)}

.site-header{position:absolute;left:0;top:0;width:1200px;height:97px;background:var(--white)}
.logo-box{position:absolute;left:48px;top:0;width:161px;height:134px;background:var(--white);z-index:3;display:flex;flex-direction:column;align-items:center;justify-content:center;text-align:center;gap:8px}
.logo-dot{width:40px;height:40px;border-radius:50%;background:var(--red)}
.logo-name{font-size:14px;font-weight:600;color:var(--brown);line-height:1.2}
.main-nav{position:absolute;top:43px;font-size:17px;color:#222}

.hero{position:absolute;left:0;top:97px;width:1200px;height:712px;background:linear-gradient(90deg,#1c1a14 0%,#3b3526 35%,#5a4a34 55%,#c9a06a 75%,#3a2f22 100%)}
.hero-eyebrow{left:47px;top:342px;font-size:21px;color:var(--white)}
.hero-title{font-size:48px;font-weight:500;color:var(--white);line-height:1}
.hero-copy{left:52px;top:488px;width:460px;font-size:17px;line-height:1.4;color:var(--white)}

.section-mark{position:absolute;width:12px;height:12px;border-radius:50%;background:var(--red)}
.section-title{position:absolute;width:1200px;text-align:center;font-size:33px;font-weight:400;color:var(--red)}

.service-card{position:absolute;top:1027px;width:342px;height:354px}
.service-card .photo{left:0;top:0;width:342px;height:301px}
.service-card .caption{position:absolute;left:0;top:301px;width:342px;height:53px;background:var(--brown);color:var(--white);font-size:26px;display:flex;align-items:center;padding-left:20px}
.service-card svg{position:absolute;right:16px;top:314px}

.events{position:absolute;left:0;top:1566px;width:1200px;height:572px;background:var(--brown)}
.events-title{left:673px;top:1630px;font-size:33px;color:var(--white)}
.events-copy{left:676px;top:1697px;width:470px;font-size:20px;line-height:1.6;color:var(--white)}
.events-list{left:684px;top:1812px;list-style:none;color:var(--white);font-size:20px}
.events-list li{position:relative;padding-left:28px;height:42px}
.events-list li::before{content:"";position:absolute;left:0;top:14px;width:8px;height:8px;border-radius:50%;background:var(--red)}

.contact-box{position:absolute;left:55px;top:3094px;width:1096px;height:547px;background:var(--brown);z-index:2}
.contact-title{position:absolute;left:0;top:34px;width:1096px;text-align:center;font-size:33px;color:var(--white)}
.field{position:absolute;left:90px;width:343px;background:var(--white);font-size:16px;color:#222;padding:14px 16px}

.site-footer{position:absolute;left:0;top:3500px;width:1200px;height:477px;background:var(--black)}
.footer-logo{position:absolute;left:50px;top:3703px;width:197px;height:197px;border-radius:50%;background:var(--white);display:flex;flex-direction:column;align-items:center;justify-content:center;gap:10px;text-align:center}
.footer-head{position:absolute;top:3708px;font-size:21px;color:var(--red)}
.footer-list{position:absolute;top:3748px;list-style:none;color:var(--white);font-size:17px}
.footer-list li{height:32px}
.footer-list.bullets li{position:relative;padding-left:19px}
.footer-list.bullets li::before{content:"";position:absolute;left:0;top:10px;width:6px;height:6px;border-radius:50%;background:var(--red)}
.copyright{position:absolute;left:0;top:3988px;width:1200px;text-align:center;font-size:16px;color:#333}
</style>
</head>
<body>

<header class="site-header">
  <div class="logo-box">
    <span class="logo-dot"></span>
    <span class="logo-name">Hickory Ember Catering</span>
  </div>
  <nav>
    <span class="main-nav" style="left:492px">Home</span>
    <span class="main-nav" style="left:574px">About Us</span>
    <span class="main-nav" style="left:681px">service</span>
    <span class="main-nav" style="left:773px">Events</span>
    <span class="main-nav" style="left:860px">Venues</span>
    <span class="main-nav" style="left:954px">Careeres</span>
    <span class="main-nav" style="left:1064px">Online Order</span>
  </nav>
</header>

<section class="hero" role="img" aria-label="Ice cream cone with sprinkles and string lights at an evening outdoor event"></section>
<p class="abs hero-eyebrow">We are Hickory Ember</p>
<h1 class="abs hero-title" style="left:48px;top:376px">FOOD IS ONLY</h1>
<h1 class="abs hero-title" style="left:137px;top:433px">THE BEGINNING</h1>
<p class="abs hero-copy">Lorem Ipsum is simply dummy text of the printing and typesetting industry</p>
<a class="btn btn-red" style="left:52px;top:550px;width:140px;height:47px">Order Now</a>

<span class="section-mark" style="left:612px;top:912px"></span>
<h2 class="section-title" style="top:942px">Our Services</h2>
<div class="service-card" style="left:52px">
  <div class="photo" role="img" aria-label="Buffet table with tiered desserts and plates" style="background:linear-gradient(160deg,#6b5a4a,#c8b8a2 50%,#8a6b4f)"></div>
  <div class="caption">Catered Events</div>
  <svg width="28" height="28" viewBox="0 0 28 28"><circle cx="14" cy="14" r="12" fill="none" stroke="#fff" stroke-width="2"/><path d="M8 14h11M15 10l4 4-4 4" fill="none" stroke="#fff" stroke-width="2"/></svg>
</div>
<div class="service-card" style="left:433px">
  <div class="photo" role="img" aria-label="Colleagues dining together at a long table" style="background:linear-gradient(180deg,#5a5a52,#3b4a2e 60%,#2f4a20)"></div>
  <div class="caption">Workplace Dining</div>
  <svg width="28" height="28" viewBox="0 0 28 28"><circle cx="14" cy="14" r="12" fill="none" stroke="#fff" stroke-width="2"/><path d="M8 14h11M15 10l4 4-4 4" fill="none" stroke="#fff" stroke-width="2"/></svg>
</div>
<div class="service-card" style="left:814px">
  <div class="photo" role="img" aria-label="Grilled vegetable and corn skewers on a plate outdoors" style="background:linear-gradient(180deg,#2f4030,#4a4a30 50%,#7a5a20)"></div>
  <div class="caption">Delivery</div>
  <svg width="28" height="28" viewBox="0 0 28 28"><circle cx="14" cy="14" r="12" fill="none" stroke="#fff" stroke-width="2"/><path d="M8 14h11M15 10l4 4-4 4" fill="none" stroke="#fff" stroke-width="2"/></svg>
</div>
<a class="btn btn-red" style="left:511px;top:1450px;width:161px;height:53px">View More</a>

<section class="events"></section>
<svg class="abs" style="left:40px;top:1640px" width="572" height="420" viewBox="0 0 572 420">
  <path d="M0 0H148V10H10V118H0Z" fill="#e1261c"/>
  <path d="M572 420H424V410H562V302H572Z" fill="#e1261c"/>
</svg>
<div class="photo" role="img" aria-label="Grilled meat skewers with sauce on a plate" style="left:48px;top:1655px;width:552px;height:393px;background:radial-gradient(circle at 55% 55%,#7a3a22,#2a2018 55%,#0f1a1e)"></div>
<span class="section-mark" style="left:749px;top:1600px"></span>
<h2 class="abs events-title">Our Events</h2>
<p class="abs events-copy">At Hickory Ember Catering and Events, we believe, like any great recipe, creating a remarkable event</p>
<ul class="abs events-list">
  <li>Weddings</li><li>Corporate</li><li>Social</li><li>Gallery</li>
</ul>
<a class="btn btn-white" style="left:677px;top:2000px;width:162px;height:53px">Read more</a>

<span class="section-mark" style="left:605px;top:2214px"></span>
<h2 class="section-title" style="top:2244px;left:20px">Our Gallery</h2>
<div class="photo" role="img" aria-label="Chocolate ice cream dessert in a bowl" style="left:59px;top:2345px;width:335px;height:285px;background:linear-gradient(160deg,#8a8a40,#5a3420 60%,#d8c8b0)"></div>
<div class="photo" role="img" aria-label="Waiter carrying a tray of desserts" style="left:411px;top:2345px;width:398px;height:585px;background:linear-gradient(160deg,#2a1e18,#1a1a1a 40%,#8a5a40 80%,#c8a890)"></div>
<div class="photo" role="img" aria-label="Buffet trays of roasted food" style="left:825px;top:2345px;width:334px;height:285px;background:linear-gradient(160deg,#5a4a40,#a86a3a 50%,#6a5a50)"></div>
<div class="photo" role="img" aria-label="Plated appetisers on a table" style="left:59px;top:2645px;width:335px;height:285px;background:linear-gradient(160deg,#3a3a2a,#2a2a2a 50%,#c86a30)"></div>
<div class="photo" role="img" aria-label="Bowls of colourful salads" style="left:825px;top:2645px;width:334px;height:285px;background:linear-gradient(180deg,#2a3a20,#b85a30 55%,#5a3018)"></div>
<a class="btn btn-red" style="left:537px;top:2981px;width:161px;height:53px">View More</a>

<footer class="site-footer"></footer>
<svg class="abs" style="left:0;top:3490px;z-index:1" width="1200" height="60" viewBox="0 0 1200 60">
  <path d="M0 0L60 30V44L0 16Z" fill="#e1261c"/>
  <path d="M1200 0L1140 30V44L1200 16Z" fill="#e1261c"/>
</svg>

<section class="contact-box">
  <h2 class="contact-title">Contact us</h2>
  <div class="field" style="top:106px;height:56px">Name</div>
  <div class="field" style="top:178px;height:56px">Email</div>
  <div class="field" style="top:250px;height:56px">Phone Number</div>
  <div class="field" style="top:322px;height:101px">Message</div>
  <a class="btn btn-red" style="left:192px;top:456px;width:111px;height:39px;font-size:15px">SEND</a>
  <div class="photo" role="img" aria-label="Smiling chef in white uniform with arms crossed" style="left:545px;top:106px;width:467px;height:367px;background:linear-gradient(180deg,#cfcfcf,#bdbdbd)"></div>
</section>

<div class="footer-logo">
  <span class="logo-dot"></span>
  <span class="logo-name" style="width:150px">Hickory Ember Catering</span>
</div>
<h3 class="footer-head" style="left:361px">Contact Links</h3>
<ul class="footer-list bullets" style="left:361px">
  <li>About</li><li>Service</li><li>Blog</li><li>Contact Us</li><li>Glads</li>
</ul>
<h3 class="footer-head" style="left:577px">Our Service</h3>
<ul class="footer-list" style="left:577px">
  <li>Catered Events</li><li>Workplace Dining</li><li>Delivery</li>
</ul>
<h3 class="footer-head" style="left:766px">Opening Hours</h3>
<ul class="footer-list" style="left:770px">
  <li>12.00 am-1.00pm</li><li>1.00am-3.00pm</li><li>10.00pm-11..pm</li>
</ul>
<h3 class="footer-head" style="left:991px">Contact Us</h3>
<div class="abs" style="left:994px;top:3753px;width:170px;height:45px;background:#fff;font-size:14px;padding:12px 10px">Name</div>
<a class="btn btn-red" style="left:994px;top:3811px;width:158px;height:44px;font-size:13px">SUBSCRIBE</a>

<p class="copyright">© 2023 Hickory Ember Catering &amp; Events. All rights reserved.</p>

</body>
</html>
```